Elegant One-Page Flyer That Catches People's Eye

For a series of workshops and zoom calls I am marketing with a colleague of mine, we would like to have an elegant, catchy one-page flyer that entices people to contact us. I am envisioning a one-page flyer (a card that is somewhat larger than a postcard) with great text, layout and images which magnetically draws people to us and is positive and inspiring. Also, if at all possible, a QR code linking it to our websites. Good colours would be shades of blue and green. I am uploading: the Text, our pictures, logos and contact information.

```html
<!DOCTYPE html>
<html lang="en">
<head>
<meta charset="utf-8">
<title>Rising Above Hidden Career Deal Breakers – Flyer</title>
<link href="https://fonts.googleapis.com/css2?family=Bebas+Neue&family=Poppins:wght@400;500;600;700;800&display=swap" rel="stylesheet">
<style>
  :root {
    --page-bg: #ffffff;
    --paper: #e7e8e9;
    --paper-light: #f0f1f1;
    --crimson: #7f0b10;
    --olive: #7c9d55;
    --ink: #2a2b2d;
    --ink-soft: #3b3c3f;
    --slate-panel: #b9c1cb;
    --rock: #6f7472;
    --sky: #c9d3d8;
    --skin-placeholder: #c8a890;
  }
  * { box-sizing: border-box; margin: 0; padding: 0; }
  html, body { width: 1200px; height: 2327px; overflow: hidden; background: var(--page-bg); }
  body { font-family: "Poppins", sans-serif; color: var(--ink); position: relative; }

  .flyer {
    position: absolute; left: 40px; top: 138px; width: 1120px; height: 2050px;
    background: linear-gradient(180deg, var(--paper-light) 0%, var(--paper) 55%, #dcdedf 100%);
    box-shadow: 0 18px 30px rgba(0,0,0,0.18);
    overflow: hidden;
  }
  .hero-photo {
    position: absolute; right: 0; top: 0; width: 640px; height: 1000px;
    background: linear-gradient(180deg, var(--sky) 0%, #9aa6a9 35%, var(--rock) 60%, #8d918f 100%);
    -webkit-mask-image: linear-gradient(90deg, transparent 0%, #000 35%), linear-gradient(180deg, #000 60%, transparent 100%);
    -webkit-mask-composite: source-in;
    mask-image: linear-gradient(90deg, transparent 0%, #000 35%), linear-gradient(180deg, #000 60%, transparent 100%);
    mask-composite: intersect;
  }
  .abs { position: absolute; }

  .eyebrow {
    left: 76px; top: 78px; color: var(--crimson); font-weight: 800;
    font-size: 43px; line-height: 41px; letter-spacing: -0.5px; white-space: nowrap;
  }
  .lead {
    left: 76px; top: 182px; font-size: 28px; line-height: 35px; color: var(--ink-soft); width: 520px;
  }
  .headline {
    left: 76px; top: 326px; font-family: "Bebas Neue", sans-serif; font-size: 80px; line-height: 74px;
    color: var(--ink); white-space: nowrap;
  }

  .offer-pill { left: 76px; top: 494px; width: 980px; height: 106px; display: flex; }
  .offer-pill .workshops {
    width: 460px; flex: none; background: var(--olive); border-radius: 53px 0 0 53px;
    font-family: "Bebas Neue", sans-serif; font-size: 62px; line-height: 1; color: #fff;
    display: flex; align-items: center; justify-content: space-between;
    padding: 6px 6px 0 20px; white-space: nowrap;
  }
  .offer-pill .plus { font-family: "Poppins", sans-serif; font-weight: 700; font-size: 46px; margin-bottom: 6px; }
  .offer-pill .sessions {
    flex: 1; background: var(--crimson); border-radius: 0 53px 53px 0;
    color: #fff; font-weight: 700; font-size: 27px; line-height: 31px;
    display: flex; align-items: center; padding-left: 46px; white-space: nowrap;
  }

  .learn {
    left: 78px; top: 624px; font-size: 28px; line-height: 34px; font-weight: 600; color: var(--ink-soft); white-space: nowrap;
  }
  .topics {
    left: 79px; top: 678px; width: 962px; height: 198px;
    border: 2px dashed var(--olive); border-top: none; border-radius: 0 0 12px 12px;
  }
  .topics::before {
    content: ""; position: absolute; top: 0; right: -2px; width: 322px; border-top: 2px dashed var(--olive);
  }
  .topic {
    position: absolute; display: flex; gap: 16px; font-size: 25px; line-height: 28px; color: var(--ink-soft); white-space: nowrap;
  }
  .topic svg { flex: none; margin-top: 3px; }

  .section-title {
    left: 0; width: 1120px; top: 890px; text-align: center;
    color: var(--crimson); font-weight: 600; font-size: 36px; letter-spacing: 6px;
  }

  .facilitator {
    left: 110px; width: 924px; height: 282px; border: 3px solid var(--ink);
    border-radius: 141px; background: rgba(225,227,228,0.7);
  }
  .facilitator .portrait {
    position: absolute; left: 10px; top: 12px; width: 256px; height: 256px; border-radius: 50%;
    background: radial-gradient(circle at 50% 40%, var(--skin-placeholder) 0%, #9b8270 55%, #e9eaea 56%);
    box-shadow: 0 0 0 6px #f4f4f4;
  }
  .facilitator .name { position: absolute; left: 304px; top: 34px; font-weight: 700; font-size: 38px; white-space: nowrap; }
  .facilitator .bio { position: absolute; left: 304px; top: 96px; font-size: 26px; line-height: 30px; color: var(--ink); white-space: nowrap; }
  .name.green { color: var(--olive); }
  .name.red { color: var(--crimson); }

  .brand { white-space: nowrap; font-weight: 400; }
  .brand-one { left: 112px; top: 1636px; font-size: 52px; color: var(--olive); display: flex; align-items: center; gap: 16px; }
  .brand-one .mark { width: 44px; height: 44px; border-radius: 50%; border: 3px solid var(--olive); }
  .brand-two { left: 640px; top: 1640px; color: var(--crimson); font-size: 40px; line-height: 44px; letter-spacing: 2px; text-align: right; }
  .brand-two .city { display: block; font-size: 22px; line-height: 22px; letter-spacing: 1px; }

  .contact-panel {
    left: 63px; top: 1782px; width: 994px; height: 221px; background: var(--slate-panel); border-radius: 22px;
  }
  .ribbon {
    left: 245px; top: 1770px; width: 630px; height: 72px; background: var(--crimson);
    border-radius: 10px 10px 24px 24px; color: #fff; font-weight: 700; font-size: 27px; line-height: 31px;
    text-align: center; padding-top: 5px; white-space: nowrap;
  }
  .contact-divider { left: 493px; top: 1870px; height: 100px; border-left: 2px dashed #8e97a2; }
  .contact { top: 1870px; font-size: 24px; line-height: 30px; color: #fff; font-weight: 500; white-space: nowrap; }
  .contact .who { color: #3f444b; font-weight: 700; font-size: 22px; margin-bottom: 4px; }
  .contact .row { display: flex; align-items: center; gap: 10px; }
  .contact-one { left: 165px; }
  .contact-two { left: 575px; }
</style>
</head>
<body>
  <main class="flyer">
    <div class="hero-photo" role="img" aria-label="Photo of a hiker standing on a rocky summit facing snowy alpine peaks"></div>

    <h2 class="abs eyebrow">IS YOUR CAREER GOING<br>THE WAY YOU WANT?</h2>
    <p class="abs lead">If not, do you feel stuck? Blocked? Frustrated? Don’t know what to do about this?</p>
    <h1 class="abs headline">RISING ABOVE HIDDEN<br>CAREER DEAL BREAKERS</h1>

    <div class="abs offer-pill">
      <div class="workshops"><span>4 MINI-WORKSHOPS</span><span class="plus">+</span></div>
      <div class="sessions">2 short Online Group Coaching<br>Sessions between Workshops</div>
    </div>

    <p class="abs learn">Learn to overcome and rise above<br>the 4 top hidden career deal breakers fast</p>
    <div class="abs topics">
      <div class="topic" style="left:20px; top:30px;">
        <svg width="20" height="20" viewBox="0 0 20 20"><circle cx="10" cy="10" r="8" fill="none" stroke="#7c9d55" stroke-width="1.5"/><path d="M6 10l3 3 5-6" fill="none" stroke="#7c9d55" stroke-width="1.5"/></svg>
        <span>Microaggressions</span>
      </div>
      <div class="topic" style="left:20px; top:86px;">
        <svg width="20" height="20" viewBox="0 0 20 20"><circle cx="10" cy="10" r="8" fill="none" stroke="#7c9d55" stroke-width="1.5"/><path d="M6 10l3 3 5-6" fill="none" stroke="#7c9d55" stroke-width="1.5"/></svg>
        <span>Workplace snakes and<br>other dysfunctional types</span>
      </div>
      <div class="topic" style="left:460px; top:34px;">
        <svg width="20" height="20" viewBox="0 0 20 20"><circle cx="10" cy="10" r="8" fill="none" stroke="#7c9d55" stroke-width="1.5"/><path d="M6 10l3 3 5-6" fill="none" stroke="#7c9d55" stroke-width="1.5"/></svg>
        <span>Toxic black box team dynamics</span>
      </div>
      <div class="topic" style="left:460px; top:90px;">
        <svg width="20" height="20" viewBox="0 0 20 20"><circle cx="10" cy="10" r="8" fill="none" stroke="#7c9d55" stroke-width="1.5"/><path d="M6 10l3 3 5-6" fill="none" stroke="#7c9d55" stroke-width="1.5"/></svg>
        <span>Disempowering Subconscious<br>Algorithms</span>
      </div>
    </div>

    <h3 class="abs section-title">FACILITATORS</h3>

    <section class="abs facilitator" style="top:965px;">
      <div class="portrait" role="img" aria-label="Portrait photo of Dr. Mara Ellwood"></div>
      <div class="name green">Dr. Mara Ellwood</div>
      <p class="bio">PhD, CPC, is an American &amp; Swiss-Trained<br>Work &amp; Organizational Psychologist,<br>ICF-Certified Coach, Board Certified<br>Hypnotherapist, Certified Naturopath (TEN)<br>&amp; Certified Ayurvedic Practitioner.</p>
    </section>

    <section class="abs facilitator" style="top:1285px;">
      <div class="portrait" role="img" aria-label="Portrait photo of Dr. Helena Vogt"></div>
      <div class="name red" style="top:50px;">Dr. Helena Vogt</div>
      <p class="bio" style="top:112px;">Ph.D., PCC is a coach and somatic<br>experience practitioner, a team coach<br>with diploma and a certified virtual<br>team coach.</p>
    </section>

    <div class="abs brand brand-one"><span class="mark"></span>PathBloom</div>
    <div class="abs brand brand-two">VogtCoaching<span class="city">Zürich</span></div>

    <div class="abs contact-panel"></div>
    <div class="abs ribbon">For dates, venue and further information<br>Contact Helena or Mara at</div>
    <div class="abs contact-divider"></div>

    <div class="abs contact contact-one">
      <div class="who">DR. MARA ELLWOOD</div>
      <div class="row"><svg width="20" height="20" viewBox="0 0 20 20"><path d="M5 2l3 4-2 2c1 3 3 5 6 6l2-2 4 3-2 3C8 18 2 12 2 4z" fill="#7f0b10"/></svg>076 000 1234</div>
      <div class="row"><svg width="20" height="16" viewBox="0 0 20 16"><rect x="1" y="1" width="18" height="14" fill="#7f0b10"/><path d="M1 1l9 8 9-8" fill="none" stroke="#fff" stroke-width="1.5"/></svg>mara@pathbloom.ch</div>
    </div>
    <div class="abs contact contact-two">
      <div class="who">DR. HELENA VOGT</div>
      <div class="row"><svg width="20" height="20" viewBox="0 0 20 20"><path d="M5 2l3 4-2 2c1 3 3 5 6 6l2-2 4 3-2 3C8 18 2 12 2 4z" fill="#7f0b10"/></svg>079 000 56 78</div>
      <div class="row"><svg width="20" height="16" viewBox="0 0 20 16"><rect x="1" y="1" width="18" height="14" fill="#7f0b10"/><path d="M1 1l9 8 9-8" fill="none" stroke="#fff" stroke-width="1.5"/></svg>helena@vogtcoaching.ch</div>
    </div>
  </main>
</body>
</html>
```